I want to create a postcard we can use as a promotional offer. We may send out to prospects or give to people at an event to get them in front of us and start to understand their business more with the hope of engaging them as clients eventually.
The offer is a Complimentary "Venture Spark Kit". (valued at $875)
The kit includes:
Fiscal Horizon Audit
45 minute Business Discovery Meeting
6 point Diagnostic Report
3 Recommendations for your Business

The headline and there look and feel we would like the design to be focused upon is "Analyze. Boost. Grow."
Include an Image(s) as you feel appropriate.
I'm thinking Headline/Mian Branding and Picture on the Front, then Offer and details of Kit and Logos etc on the Back.

Include 2 logos as we are part of a joint operation, Meridale Accountants & Trovenly.

Call to action to Phone 0255501872 or email hello@trovenly.com.au

Logo's uploaded, committed payment, increased deadline.

Target Market(s)

Small to Medium Business

Industry/Entity Type

Business

Requirements
Must have
• Logos in Colour on Back with rest of Detail.
Front to be all about the key message "Analyze. Boost. Grow." select pic to represent.
Must create cut through and intrigue to make the holder tunr the card and read.

```html
<!DOCTYPE html>
<html lang="en">
<head>
<meta charset="utf-8">
<title>Venture Spark Kit Postcard</title>
<link rel="stylesheet" href="https://fonts.googleapis.com/css2?family=Michroma&family=PT+Sans:wght@400;700&display=swap">
<style>
  :root {
    --page-bg: #ececec;
    --card-white: #ffffff;
    --navy-deep: #1b2748;
    --navy-mid: #3a4f7e;
    --steel-blue: #6f86b4;
    --ribbon-light: #8fd3f4;
    --ribbon-mid: #3fa9e0;
    --ribbon-dark: #1a7fc0;
    --ribbon-fold: #0f5d8f;
    --ink-dark: #1f2a3a;
    --ink-navy: #1a2a5e;
    --offer-blue: #2577b5;
    --offer-green: #4caf3b;
    --panel-grey-top: #c9cacc;
    --panel-grey-bottom: #ffffff;
    --line-grey: #8a8a8a;
    --icon-blue: #1e5f9a;
    --icon-green: #3f9f3a;
  }
  * { box-sizing: border-box; margin: 0; padding: 0; }
  html, body { width: 1103px; height: 1200px; overflow: hidden; }
  body {
    background: var(--page-bg);
    font-family: "PT Sans", sans-serif;
    position: relative;
  }
  .postcard {
    position: absolute;
    left: 201px;
    width: 700px;
    height: 520px;
    background: var(--card-white);
    overflow: hidden;
  }
  .postcard--front { top: 50px; }
  .postcard--back { top: 630px; }

  /* Front */
  .hero-photo {
    position: absolute; inset: 0;
    background:
      radial-gradient(circle at 42% 62%, rgba(255,255,255,0.55) 0, rgba(180,200,235,0.25) 8%, transparent 22%),
      linear-gradient(120deg, var(--navy-deep) 0%, var(--navy-mid) 40%, var(--steel-blue) 70%, var(--navy-deep) 100%);
  }
  .headline-ribbon {
    position: absolute; left: 0; top: 14px; width: 700px; height: 90px;
  }
  .headline {
    position: absolute; left: 0; top: 26px; width: 700px; height: 62px;
    display: flex; align-items: center; justify-content: center;
    font-family: "Michroma", sans-serif;
    font-size: 30px;
    letter-spacing: 0.5px;
    color: var(--navy-deep);
    white-space: nowrap;
  }
  .headline .sep { font-size: 16px; margin: 0 10px; font-family: "PT Sans", sans-serif; font-weight: 700; }

  /* Back */
  .offer-panel {
    position: absolute; left: 8px; top: 0; width: 340px; height: 520px;
    background: linear-gradient(to bottom, var(--panel-grey-top) 0%, #e3e4e5 55%, var(--panel-grey-bottom) 85%);
  }
  .kit-ribbon { position: absolute; left: 0; top: 44px; width: 345px; height: 50px; }
  .kit-title {
    position: absolute; left: 14px; top: 48px; width: 320px; height: 40px;
    display: flex; align-items: center; justify-content: center;
    font-family: "Michroma", sans-serif; font-size: 18px; color: var(--navy-deep);
    white-space: nowrap;
  }
  .kit-heading {
    position: absolute; left: 30px; top: 130px;
    font-weight: 700; font-size: 17px; color: var(--ink-dark);
  }
  .kit-list {
    position: absolute; left: 30px; top: 162px; list-style: none;
    font-size: 16px; font-weight: 700; color: var(--ink-dark); line-height: 30px;
  }
  .kit-list li::before { content: "» "; }
  .kit-icons { position: absolute; left: 0; top: 292px; width: 345px; height: 48px; }
  .contact {
    position: absolute; left: 30px; font-size: 16px; font-weight: 700; color: var(--ink-dark);
  }
  .contact--phone { top: 376px; }
  .contact--email { top: 406px; }
  .partner-names {
    position: absolute; left: 30px; top: 452px; width: 310px;
    display: flex; align-items: center; justify-content: space-between;
  }
  .partner { font-weight: 700; font-size: 17px; display: flex; align-items: center; gap: 6px; }
  .partner--accountants { color: var(--ink-navy); }
  .partner--trovenly { color: var(--offer-green); }
  .partner-mark { width: 14px; height: 14px; background: var(--offer-green); display: inline-block; }

  .free-offer {
    position: absolute; left: 387px; top: 50px;
    font-weight: 700; font-size: 22px; color: var(--offer-blue);
  }
  .offer-value {
    position: absolute; left: 402px; top: 80px;
    font-weight: 700; font-size: 15px; color: var(--offer-green);
  }
  .stamp-box {
    position: absolute; left: 532px; top: 27px; width: 111px; height: 112px;
    border: 1.5px solid var(--line-grey);
  }
  .address-line {
    position: absolute; left: 410px; width: 233px; height: 0;
    border-top: 1.5px solid var(--line-grey);
  }
  .address-line--1 { top: 211px; }
  .address-line--2 { top: 261px; }
  .address-line--3 { top: 311px; }
</style>
</head>
<body>

<section class="postcard postcard--front">
  <div class="hero-photo" role="img" aria-label="Businessman in a dark suit touching floating glass interface panels in front of server racks"></div>
  <svg class="headline-ribbon" viewBox="0 0 700 90" aria-hidden="true">
    <defs>
      <linearGradient id="headlineFill" x1="0" y1="0" x2="0" y2="1">
        <stop offset="0" stop-color="var(--ribbon-light)"/>
        <stop offset="0.6" stop-color="var(--ribbon-mid)"/>
        <stop offset="1" stop-color="var(--ribbon-dark)"/>
      </linearGradient>
    </defs>
    <path d="M0 12 H690 Q700 12 700 22 V74 H0 Z" fill="url(#headlineFill)"/>
    <path d="M678 74 H700 V84 Z" fill="var(--ribbon-fold)"/>
  </svg>
  <div class="headline">ANALYZE<span class="sep">»</span>BOOST<span class="sep">»</span>GROW</div>
</section>

<section class="postcard postcard--back">
  <div class="offer-panel"></div>
  <svg class="kit-ribbon" viewBox="0 0 345 50" aria-hidden="true">
    <defs>
      <linearGradient id="kitFill" x1="0" y1="0" x2="0" y2="1">
        <stop offset="0" stop-color="var(--ribbon-light)"/>
        <stop offset="0.6" stop-color="var(--ribbon-mid)"/>
        <stop offset="1" stop-color="var(--ribbon-dark)"/>
      </linearGradient>
    </defs>
    <path d="M12 4 H336 Q344 4 344 12 V42 H12 Z" fill="url(#kitFill)"/>
    <path d="M0 10 H12 V48 H0 Q6 29 0 10 Z" fill="var(--ribbon-dark)"/>
    <path d="M12 42 H20 L12 50 Z" fill="var(--ribbon-fold)"/>
  </svg>
  <div class="kit-title">VENTURE SPARK KIT</div>

  <p class="kit-heading">THE KIT INCLUDES:</p>
  <ul class="kit-list">
    <li>Fiscal Horizon Audit</li>
    <li>Business Discovery Meeting</li>
    <li>6 point Diagnostic Report</li>
    <li>3 Recommendations for your Business</li>
  </ul>

  <svg class="kit-icons" viewBox="0 0 345 48" aria-hidden="true">
    <g stroke="#ffffff" stroke-width="3" fill="none" stroke-linecap="round" stroke-linejoin="round">
      <circle cx="91" cy="24" r="21" fill="var(--icon-blue)" stroke="none"/>
      <path d="M82 24 L89 31 L101 16"/>
      <circle cx="153" cy="24" r="21" fill="var(--icon-green)" stroke="none"/>
      <path d="M145 32 V22 M153 32 V16 M161 32 V26"/>
      <circle cx="212" cy="24" r="21" fill="var(--icon-blue)" stroke="none"/>
      <circle cx="212" cy="22" r="7"/>
      <path d="M217 27 L222 32"/>
      <circle cx="280" cy="24" r="21" fill="var(--icon-green)" stroke="none"/>
      <path d="M270 30 L278 22 L283 27 L291 18 M286 18 H291 V23"/>
    </g>
  </svg>

  <p class="contact contact--phone">Phone: 0255501872</p>
  <p class="contact contact--email">email: hello@trovenly.com.au</p>

  <div class="partner-names">
    <span class="partner partner--accountants">Meridale Accountants</span>
    <span class="partner partner--trovenly"><span class="partner-mark"></span>Trovenly</span>
  </div>

  <p class="free-offer">FREE OFFER</p>
  <p class="offer-value">valued at $875</p>
  <div class="stamp-box"></div>
  <div class="address-line address-line--1"></div>
  <div class="address-line address-line--2"></div>
  <div class="address-line address-line--3"></div>
</section>

</body>
</html>
```